Commercial Construction Company

We need a business card design based on our current logo. We are a commercial general contractor based in Southern California that specializes in bank remodels. We would like to see designs that incorporate dark blue. The final design should portray an image of professionalism and quality.

If possible, I would like to add metallic foil to the design. Thank you

```html
<!DOCTYPE html>
<html lang="en">
<head>
<meta charset="utf-8">
<title>Business Card – Front and Back</title>
<link rel="stylesheet" href="https://fonts.googleapis.com/css2?family=Montserrat:wght@400;700;800&display=swap">
<style>
  :root {
    --page-bg: #e0e0e0;
    --card-bg: #ffffff;
    --brand-blue: #1a4a80;
    --band-grey: #b8bfcb;
    --ink: #1b1b1b;
    --mark-ink: #111111;
  }
  * { box-sizing: border-box; margin: 0; padding: 0; }
  html, body {
    width: 1200px; height: 1200px; overflow: hidden;
    background: var(--page-bg);
    font-family: "Montserrat", Arial, sans-serif;
  }
  .card {
    position: absolute;
    background: var(--card-bg);
    box-shadow: 0 6px 18px rgba(0,0,0,0.35);
    overflow: hidden;
  }
  .card--front { left: 107px; top: 50px; width: 951px; height: 543px; }
  .card--back  { left: 111px; top: 619px; width: 933px; height: 531px; }

  .name-accent {
    position: absolute; left: 0; top: 242px; width: 26px; height: 60px;
    background: var(--brand-blue);
  }
  .company-name {
    position: absolute; left: 36px; top: 232px;
    color: var(--brand-blue); font-weight: 800; font-size: 35px; letter-spacing: 0.5px;
  }
  .company-suffix {
    position: absolute; left: 36px; top: 277px;
    color: var(--brand-blue); font-weight: 400; font-size: 24px;
  }

  .contact-list { position: absolute; left: 34px; top: 362px; list-style: none; }
  .contact-item {
    display: flex; align-items: center; height: 34.5px;
    font-size: 25px; color: var(--ink); white-space: nowrap;
  }
  .contact-icon { width: 24px; height: 22px; margin-right: 14px; flex: none; }

  .address {
    position: absolute; left: 582px; top: 460px;
    display: flex; align-items: center; font-size: 25px; color: var(--ink); white-space: nowrap;
  }
  .address .contact-icon { width: 24px; height: 32px; margin-right: 13px; }

  .band-blue { position: absolute; left: 0; bottom: 0; width: 476px; height: 34px; background: var(--brand-blue); }
  .band-grey { position: absolute; left: 476px; bottom: 0; right: 0; height: 34px; background: var(--band-grey); }

  .brand-mark {
    position: absolute; display: flex; align-items: center; gap: 12px;
    color: var(--mark-ink); font-weight: 800; white-space: nowrap;
  }
  .brand-mark .mark-dot { border-radius: 50%; background: var(--brand-blue); flex: none; }
  .card--front .brand-mark { left: 572px; top: 150px; font-size: 31px; }
  .card--front .mark-dot { width: 46px; height: 46px; }
  .card--back .brand-mark { left: 290px; top: 232px; font-size: 33px; }
  .card--back .mark-dot { width: 50px; height: 50px; }
</style>
</head>
<body>
  <section class="card card--front" aria-label="Card front">
    <div class="brand-mark"><span class="mark-dot"></span>HARLAN BUILD</div>

    <div class="name-accent"></div>
    <h1 class="company-name">AUTOVELA</h1>
    <p class="company-suffix">LDA</p>

    <ul class="contact-list">
      <li class="contact-item">
        <svg class="contact-icon" viewBox="0 0 24 22" aria-hidden="true">
          <path fill="var(--brand-blue)" d="M1 7c0-3 5-5 11-5s11 2 11 5v2h-6V6H7v3H1zM6 10h12l3 10H3z"/>
        </svg>215550147
      </li>
      <li class="contact-item">
        <svg class="contact-icon" viewBox="0 0 24 22" aria-hidden="true">
          <path fill="none" stroke="var(--brand-blue)" stroke-width="2.4" stroke-linejoin="round" d="M3 3l4-1 2 5-2 2c1 3 4 6 7 7l2-2 5 2-1 4c-9 0-17-8-17-17z"/>
          <path fill="none" stroke="var(--brand-blue)" stroke-width="2" d="M14 2a8 8 0 0 1 7 7M14 6a4 4 0 0 1 3 3"/>
        </svg>+351 215550147
      </li>
      <li class="contact-item">
        <svg class="contact-icon" viewBox="0 0 24 22" aria-hidden="true">
          <rect x="0" y="3" width="24" height="16" fill="var(--brand-blue)"/>
          <path fill="none" stroke="#fff" stroke-width="2" d="M1 4l11 9 11-9M1 18l8-7M23 18l-8-7"/>
        </svg>autovela.mail@example.com
      </li>
      <li class="contact-item">
        <svg class="contact-icon" viewBox="0 0 24 22" aria-hidden="true">
          <rect x="1" y="0" width="22" height="22" rx="3" fill="var(--brand-blue)"/>
        </svg>www.social.example/autovela
      </li>
    </ul>

    <div class="address">
      <svg class="contact-icon" viewBox="0 0 24 32" aria-hidden="true">
        <path fill="var(--brand-blue)" d="M12 0a11 11 0 0 1 11 11c0 8-11 21-11 21S1 19 1 11A11 11 0 0 1 12 0z"/>
        <circle cx="12" cy="11" r="5" fill="#fff"/>
      </svg>Rua das Oliveiras, 42
    </div>

    <div class="band-blue"></div>
    <div class="band-grey"></div>
  </section>

  <section class="card card--back" aria-label="Card back">
    <div class="brand-mark"><span class="mark-dot"></span>HARLAN BUILD</div>
  </section>
</body>
</html>
```